Cover design needed for scholarship book whose intended audience is students with medical conditions

I need a book cover designed for a book called, “The Thistle Grant: How To Make Your Health Challenge Pay Your Way Through School.” This book is aimed at students with a variety of medical conditions. I wrote The Thistle Grant after I received a medical-based scholarship ($96,000) to attend college and law school based on my allergies to pollen—hence the title. However, this government program applies to just about any medical condition—not just allergies. I have assisted students in applying for this program who suffer from many different medical conditions. So I would like the cover design to convey that message—that this program applies to many different medical conditions. One of the big misconceptions about medical-based scholarships is you will only qualify if you have a really serious medical condition. So I would like to see some cover designs that list some common medical conditions in order to convey to the reader that many different medical conditions qualify. A few possible medical conditions are allergies, asthma, ADHD, depression, anxiety, back pain, eating disorders, bipolar, sleep disorders, and OCD. Possible ways to convey this may be to have the names of some of these common medical conditions written on graduation caps or randomly dispersed in the background, etc. However, this isn’t the only theme I would like to see. In essence, I give you creative liberty to wow me with your design prowess. The point of crowd design is to get variety of designs to choose from that I may not have thought of on my own. I have dabbled with some ideas that blend the themes of the education world and the medical world and I think this is the essence of the book. What ever you come up with, it needs to make it clear at a glance that this book helps you pay for college on the basis of your medical condition—whatever medical condition that may be. To see a simple mock up I did (that I don't want to use) go to healthtuitionaid.example

The book is 153 pages on 5x8 paper. I am planning to print the book through PrintHarbor, so the cover should adhere to the PrintHarbor design requirements. I can provide the PrintHarbor template if needed.

Updates: Please be able to provide a few updates to the cover design if your design is selected. After choosing the final design, physical proofs of the book will be ordered so I can see what your design looks like in real life. After the proofs are reviewed, I may need some minor changes (i.e., maybe the back cover text needs a new font size, etc..) Also, after I use the proofs to solicit endorsements, I am planning to purchase my own ISBN number and barcode. I would like the designer to be able to update my cover to include a new ISBN and barcode after the initial proofs are printed which should be 3-4 weeks later. So please be able to provide a few updates to the cover design if your design is selected.

Target Market(s)

Students/parents who are planning to attend college and have some type of medical condition

Industry/Entity Type

College

Font styles to use
Serif

Requirements
Must have
• My project must have a general education/medical theme
Nice to have
• I'd like to see some designs that include random medical conditions dispersed on the cover. Maybe a different medical condition written on several different graduation caps, or some other context.
Should not have
• The cover design should not depict persons with severe medical conditions--i.e., people in wheelchairs, hospital beds, etc.

```html
<!DOCTYPE html>
<html lang="en">
<head>
<meta charset="utf-8">
<title>The Thistle Grant – Book Cover</title>
<link rel="stylesheet" href="https://fonts.googleapis.com/css2?family=Bebas+Neue&family=Oswald:wght@500;600&family=Graduate&family=Special+Elite&display=swap">
<style>
  :root {
    --page-bg: #d9d9d9;
    --cover-yellow: #f5bb10;
    --cover-yellow-light: #f9cf2c;
    --hex-yellow: #f8c81c;
    --hex-line: #e0a40a;
    --title-brown: #6a4a30;
    --teal: #3f6e7c;
    --teal-band: #4b7c87;
    --band-text: #e6eef0;
    --author-yellow: #f7c21a;
    --label-grey: #8a7c55;
    --faint: rgba(255, 230, 120, 0.55);
  }
  * { box-sizing: border-box; margin: 0; padding: 0; }
  html, body { width: 1200px; height: 900px; overflow: hidden; }
  body {
    background: var(--page-bg);
    position: relative;
  }
  .book-cover {
    position: absolute;
    left: 344px;
    top: 40px;
    width: 512px;
    height: 820px;
    background: linear-gradient(160deg, var(--cover-yellow-light) 0%, var(--cover-yellow) 55%, #f2b208 100%);
    overflow: hidden;
  }
  .cover-art {
    position: absolute;
    inset: 0;
    width: 512px;
    height: 820px;
  }
  .title-block {
    position: absolute;
    left: 40px;
    right: 28px;
    top: 50px;
    text-align: right;
  }
  .series-title {
    font-family: "Oswald", sans-serif;
    font-weight: 600;
    font-size: 40px;
    line-height: 1;
    color: var(--title-brown);
    letter-spacing: 0.5px;
  }
  .subtitle-lead {
    font-family: "Oswald", sans-serif;
    font-weight: 500;
    font-size: 19px;
    line-height: 1.3;
    color: var(--teal);
    margin-top: 6px;
  }
  .headline {
    font-family: "Bebas Neue", sans-serif;
    font-size: 88px;
    line-height: 0.9;
    color: var(--teal);
    text-align: left;
    margin-top: 10px;
  }
  .headline-tail {
    font-family: "Graduate", serif;
    font-size: 40px;
    line-height: 1.1;
    color: var(--teal);
    text-align: right;
  }
  .cover-band {
    position: absolute;
    left: 0;
    right: 0;
    bottom: 0;
    height: 84px;
    background: var(--teal-band);
    text-align: center;
    padding-top: 18px;
  }
  .band-tagline {
    font-family: "Special Elite", monospace;
    font-size: 14px;
    letter-spacing: 2.5px;
    color: var(--band-text);
  }
  .band-author {
    font-family: "Graduate", serif;
    font-size: 19px;
    letter-spacing: 1px;
    color: var(--author-yellow);
    margin-top: 6px;
  }
  .hex-label {
    font-family: "Oswald", sans-serif;
    font-weight: 600;
    font-size: 21px;
    fill: var(--label-grey);
    text-anchor: middle;
  }
  .dollar-mark {
    font-family: "Oswald", sans-serif;
    font-size: 30px;
    fill: var(--faint);
  }
</style>
</head>
<body>
  <div class="book-cover">
    <svg class="cover-art" viewBox="0 0 512 820" xmlns="http://www.w3.org/2000/svg">
      <defs>
        <polygon id="hex-cell" points="0,-70 60.6,-35 60.6,35 0,70 -60.6,35 -60.6,-35"/>
        <marker id="arrow-tip" viewBox="0 0 10 10" refX="5" refY="5" markerWidth="6" markerHeight="6" orient="auto-start-reverse">
          <path d="M0,0 L10,5 L0,10 z" fill="#b98a2a"/>
        </marker>
      </defs>

      <g class="medical-crosses" fill="var(--faint)">
        <rect x="395" y="180" width="14" height="44"/><rect x="380" y="195" width="44" height="14"/>
        <rect x="40" y="290" width="14" height="44"/><rect x="25" y="305" width="44" height="14"/>
        <rect x="445" y="330" width="14" height="44"/><rect x="430" y="345" width="44" height="14"/>
        <rect x="445" y="470" width="14" height="44"/><rect x="430" y="485" width="44" height="14"/>
      </g>
      <g class="dollar-marks">
        <text class="dollar-mark" x="30" y="380">$</text>
        <text class="dollar-mark" x="80" y="335">$</text>
        <text class="dollar-mark" x="210" y="330">$</text>
        <text class="dollar-mark" x="395" y="370">$</text>
        <text class="dollar-mark" x="475" y="430">$</text>
      </g>

      <g class="flow-arrows" stroke="#b98a2a" stroke-width="1.3" stroke-dasharray="3 3" fill="none">
        <line x1="256" y1="450" x2="256" y2="320" marker-end="url(#arrow-tip)"/>
        <line x1="256" y1="590" x2="256" y2="740" marker-end="url(#arrow-tip)"/>
        <line x1="160" y1="510" x2="40" y2="445" marker-end="url(#arrow-tip)"/>
        <line x1="352" y1="510" x2="480" y2="445" marker-end="url(#arrow-tip)"/>
        <line x1="160" y1="630" x2="40" y2="690" marker-end="url(#arrow-tip)"/>
        <line x1="352" y1="630" x2="480" y2="700" marker-end="url(#arrow-tip)"/>
        <line x1="40" y1="445" x2="40" y2="370" marker-end="url(#arrow-tip)"/>
        <line x1="470" y1="560" x2="470" y2="660" marker-end="url(#arrow-tip)"/>
      </g>

      <g class="condition-hexes" fill="var(--hex-yellow)" stroke="var(--hex-line)" stroke-width="1">
        <use href="#hex-cell" x="191" y="448"/>
        <use href="#hex-cell" x="321" y="448"/>
        <use href="#hex-cell" x="126" y="561"/>
        <use href="#hex-cell" x="386" y="561"/>
        <use href="#hex-cell" x="191" y="674"/>
        <use href="#hex-cell" x="321" y="674"/>
        <use href="#hex-cell" x="256" y="561"/>
      </g>

      <g class="graduate-emblem" role="img" aria-label="Graduate in cap holding a diploma, flanked by dollar signs">
        <polygon points="256,501 308,531 308,591 256,621 204,591 204,531" fill="var(--teal)" opacity="0.85"/>
      </g>

      <text class="hex-label" x="191" y="470">ADHD</text>
      <text class="hex-label" x="321" y="470">ASTHMA</text>
      <text class="hex-label" x="126" y="584">DEPRESSION</text>
      <text class="hex-label" x="386" y="584">ALLERGIES</text>
      <text class="hex-label" x="191" y="697">DIABETES</text>
      <text class="hex-label" x="321" y="697">ANXIETY</text>
    </svg>

    <header class="title-block">
      <h1 class="series-title">THE THISTLE GRANT</h1>
      <p class="subtitle-lead">HOW TO MAKE YOUR HEALTH CHALLENGE</p>
      <p class="headline">PAY YOUR WAY</p>
      <p class="headline-tail">THROUGH SCHOOL</p>
    </header>

    <footer class="cover-band">
      <p class="band-tagline">100'S OF MEDICAL CONDITIONS, MILLIONS OF DOLLARS</p>
      <p class="band-author">MARCUS HALE</p>
    </footer>
  </div>
</body>
</html>
```